Flyer for photo scanning business

Hello,
I need a flyer created for my business that would be suitable for print, to drop in letterboxes in my local community.

I would like the flyer to convey very simply the services I offer which is scanning negatives, slides and VHS tapes to digital files.
Hopefully it can make it look like an easy process, as people are often daunted by the task of sorting through old photos so they don't always get around to having them scanned.

I have a pinned facebook post that can be used by the designer to reference my services. Pricing does not need to be included on the flyer.
http://facebook.com/lanternloftmedia

Target Market(s)

Parents & Grandparents

Requirements
Must have
• Must make my services look simple! Refer to pinned facebook post for detailed outline of my services.

I would like to flyer to point towards my contact details -
www.lanternloft.com
Miriam 0482 917 356

Colours in line with my logo/brand (uploaded to brief).
Nice to have
• Stock images of 35mm film negatives, 8mm film, VHS tapes, or Velmaprint slides would be worth including. I have also uploaded a mockup of the USB sticks that I provide with digitised images.
Should not have
• no prices needed,

```html
<!DOCTYPE html>
<html lang="en">
<head>
<meta charset="utf-8">
<title>Lanternloft Media – Scanning Flyer</title>
<link href="https://fonts.googleapis.com/css2?family=Montserrat:wght@500;600;800&family=Open+Sans:wght@300;400&family=Oswald:wght@500&family=Cookie&display=swap" rel="stylesheet">
<style>
  :root{
    --page:#e9eaec;
    --navy:#151b2c;
    --brand:#4a7aab;
    --brand-deep:#2f62a0;
    --brand-light:#6fb0df;
    --sky:#5aa7d9;
    --yellow:#f6ec1a;
    --ink:#1d1d1f;
    --white:#ffffff;
    --black:#000000;
  }
  *{box-sizing:border-box;margin:0;padding:0}
  html,body{width:1200px;height:1200px;overflow:hidden;background:var(--page)}
  .flyer{position:absolute;left:188px;top:20px;width:824px;height:1160px;background:var(--white);overflow:hidden;font-family:"Open Sans",sans-serif;color:var(--ink)}

  .photo-band{position:absolute;left:0;top:0;width:824px;height:262px;display:flex}
  .photo{height:100%}
  .photo--reels{width:412px;background:linear-gradient(135deg,#1a2032,#2a2f3a 55%,#151a28)}
  .photo--slides{width:200px;background:linear-gradient(135deg,#e43a30,#f1d22a 45%,#62b7e0 75%,#2a2a30)}
  .photo--tapes{width:212px;background:linear-gradient(135deg,#e8dcc4,#b6603a 50%,#2c2a2a)}
  .brand{position:absolute;left:0;top:0;width:412px;height:262px;display:flex;flex-direction:column;align-items:center;justify-content:center;gap:16px}
  .brand__dot{width:70px;height:70px;border-radius:50%;background:var(--brand-light)}
  .brand__name{font-family:"Open Sans",sans-serif;font-weight:300;font-size:27px;letter-spacing:6px;color:var(--white);text-align:center;line-height:1.35}

  .hero{position:absolute;left:0;top:262px;width:824px;height:595px;background:var(--brand)}
  .hero__glow{position:absolute;right:0;top:0;width:420px;height:270px;background:radial-gradient(ellipse at 70% 50%,#7aa3c9 0%,rgba(74,122,171,0) 70%)}
  .usb{position:absolute;left:566px;top:52px;width:226px;height:160px;border-radius:14px;background:linear-gradient(135deg,#f4f6f8 0%,#9fb9d4 45%,#4f7fb0 100%)}
  .headline{position:absolute;left:46px;top:34px;z-index:1;font-family:"Montserrat",sans-serif;font-weight:800;font-size:35px;line-height:39px;color:var(--white);letter-spacing:.2px;white-space:nowrap}
  .headline__accent{color:var(--yellow)}
  .promise{position:absolute;left:46px;top:162px;z-index:1;font-family:"Cookie",cursive;font-size:33px;line-height:35px;color:var(--white)}

  .steps{position:absolute;left:42px;top:272px;width:740px}
  .step{position:absolute;left:0;width:740px;background:var(--white);border-radius:40px;border:3px solid var(--white);box-shadow:0 0 0 1px #e5edf5 inset;display:flex;align-items:center}
  .step--one{top:0;height:80px}
  .step--two{top:92px;height:80px}
  .step--three{top:184px;height:106px;border-radius:48px}
  .step__badge{position:absolute;left:0;top:0;height:100%;width:174px}
  .step__label{position:absolute;left:24px;top:50%;transform:translateY(-50%);display:flex;align-items:center;gap:14px;color:var(--white)}
  .step__word{font-family:"Montserrat",sans-serif;font-weight:500;font-size:21px}
  .step__num{font-family:"Oswald",sans-serif;font-weight:500;font-size:50px;line-height:1}
  .step__text{margin-left:188px;margin-right:22px;font-size:17.5px;line-height:26px;color:var(--ink)}

  .technical{position:absolute;left:0;top:857px;width:824px;height:210px;background:var(--white)}
  .technical__title{position:absolute;left:0;right:0;top:22px;text-align:center;font-family:"Montserrat",sans-serif;font-weight:600;font-size:19px;color:var(--sky)}
  .technical__cols{position:absolute;left:38px;top:58px;width:750px;display:flex}
  .technical__col{flex:1;text-align:center;font-size:14px;line-height:22.5px;padding:0 12px;letter-spacing:-.2px}
  .technical__col + .technical__col{border-left:1.5px solid var(--ink)}
  .technical__col--middle{padding:0 24px}

  .footer{position:absolute;left:0;top:1067px;width:824px;height:93px}
  .footer__shape{position:absolute;inset:0}
  .footer__web{position:absolute;left:46px;top:22px;font-family:"Montserrat",sans-serif;font-weight:600;font-size:26px;color:var(--white)}
  .footer__web span{color:var(--sky)}
  .footer__phone{position:absolute;right:44px;top:26px;font-family:"Montserrat",sans-serif;font-weight:600;font-size:27px;color:var(--white)}
</style>
</head>
<body>
<main class="flyer">
  <section class="photo-band">
    <div class="photo photo--reels" role="img" aria-label="Pile of old film reels and canisters"></div>
    <div class="photo photo--slides" role="img" aria-label="Heap of colourful plastic slide mounts"></div>
    <div class="photo photo--tapes" role="img" aria-label="VHS tapes and sleeves on a wooden table"></div>
    <div class="brand">
      <div class="brand__dot"></div>
      <div class="brand__name">LANTERNLOFT<br>MEDIA</div>
    </div>
  </section>

  <section class="hero">
    <div class="hero__glow"></div>
    <div class="usb" role="img" aria-label="Two branded USB sticks, one white and one blue"></div>
    <h1 class="headline">SCANNING NEGATIVES,<br>SLIDES AND VHS TAPES<br>TO <span class="headline__accent">DIGITAL FILES</span></h1>
    <p class="promise">I promise to make it very easy for you to<br>keep your precious memories forever.</p>

    <div class="steps">
      <div class="step step--one">
        <svg class="step__badge" viewBox="0 0 174 80" preserveAspectRatio="none" aria-hidden="true">
          <defs><linearGradient id="badgeA" x1="0" x2="1"><stop offset="0" stop-color="#6fb0df"/><stop offset="1" stop-color="#2f62a0"/></linearGradient></defs>
          <path d="M38 4 H150 L172 40 L150 76 H38 A36 36 0 0 1 38 4 Z" fill="url(#badgeA)"/>
        </svg>
        <div class="step__label"><span class="step__word">STEP</span><span class="step__num">01</span></div>
        <p class="step__text">Find your old negatives or tapes and organise them as much or as little as you want.</p>
      </div>
      <div class="step step--two">
        <svg class="step__badge" viewBox="0 0 174 80" preserveAspectRatio="none" aria-hidden="true">
          <path d="M38 4 H150 L172 40 L150 76 H38 A36 36 0 0 1 38 4 Z" fill="url(#badgeA)"/>
        </svg>
        <div class="step__label"><span class="step__word">STEP</span><span class="step__num">02</span></div>
        <p class="step__text">Contact me here or email miriam@lanternloft.com and I will come and collect these from your home in the hills area.</p>
      </div>
      <div class="step step--three">
        <svg class="step__badge" viewBox="0 0 174 106" preserveAspectRatio="none" aria-hidden="true">
          <path d="M48 4 H150 L172 53 L150 102 H48 A46 49 0 0 1 48 4 Z" fill="url(#badgeA)"/>
        </svg>
        <div class="step__label"><span class="step__word">STEP</span><span class="step__num">03</span></div>
        <p class="step__text">Once completed (usually within a few days) I will drop back your box of memories with a USB stick containing high resolution JPEG files. Contactless payment will be processed when I arrive.</p>
      </div>
    </div>
  </section>

  <section class="technical">
    <h2 class="technical__title">TECHNICAL THINGS</h2>
    <div class="technical__cols">
      <p class="technical__col">Every frame is physically cleaned and examined before scanning to ensure the best possible result. I then use an additional infra-red scanning technique to further reduce dust and scratches.</p>
      <p class="technical__col technical__col--middle">JPEG files are supplied at 2400 dpi which means you can easily print or enlarge your photos. They also look great on a 4k screen!</p>
      <p class="technical__col">VHS tapes are upscaled and captured at HD 1080p in a 100% digital workflow ensuring the best possibly quality and playback on your computer.</p>
    </div>
  </section>

  <footer class="footer">
    <svg class="footer__shape" viewBox="0 0 824 93" preserveAspectRatio="none" aria-hidden="true">
      <defs><linearGradient id="footBlue" x1="0" y1="0" x2="0" y2="1"><stop offset="0" stop-color="#6fb0df"/><stop offset="1" stop-color="#3f72aa"/></linearGradient></defs>
      <path d="M440 0 H824 V93 H0 V88 H380 Q392 88 398 80 Z" fill="url(#footBlue)"/>
      <path d="M0 0 H435 L385 70 Q378 78 366 78 H0 Z" fill="var(--black)"/>
      <path d="M0 80 H368 Q384 80 392 70 L440 2" fill="none" stroke="var(--white)" stroke-width="3"/>
    </svg>
    <div class="footer__web">www.<span>lanternloft</span>.com</div>
    <div class="footer__phone">Miriam 0482 917 356</div>
  </footer>
</main>
</body>
</html>
```